Business card design needed

I need a business card for a new company based in Perth, Western Australia, called KT Power Pty Ltd.

I'm the sole proprietor, and have 25 years' experience in directorship, senior commercial/business development/strategy roles in the oil & gas industry with both supermajors and junior listed companies. I also have interests in renewable energy (and am co-founder and director of a separate renewable energy start-up company). KT Power will be the vehicle for me to contract my services, principally in the oil & gas industry (although this will include directorship services to the renewable energy company). These services will include general consultancy in my areas of expertise, and contracting to provide senior management/director services to start-up or junior oil and gas companies.

I'm looking for a design that communicates professionalism, dynamism, experience, strategic skills and growth.

My ConnectHub profile may also be useful context;

"I have a real passion for discovering new investment opportunities and turning them from talk into reality. Right now my focus is on oil, gas and energy ventures. I’m always on the look out for compelling new investment opportunities where I can bring my leadership and strategic insight to bear to make a real difference by delivering transformational results.

I spent 24 years with HX where I built up extensive international experience in oil, gas and energy and was a member of the company’s “fast track” development programme. As an entrepreneurial senior commercial leader, strategic thinker and tactical dealmaker I was responsible for numerous deals such as divestments, farm-ins, asset swaps, new acreage bids, unitizations, gas and LNG sales, creating billions of dollars of value for HX. These deals frequently broke new ground and/or required an innovative approach that delivered results in excess of what the business thought achievable. I have held senior executive and director roles covering Exploration & Production, Mergers & Acquisitions, Business Development, LNG Marketing, Joint Venture Management, Gas & Power and Corporate head office. International assignments included UK, Australia, Indonesia, Norway & Belgium.

I’m a member of the Guild of Global Fuel Brokers (GGFB) and the Southern Council of Board Members (SCBM).

Board experience comprises four directorships and two alternate directorships of Australian companies, and directorship of a Not for Profit organisation.

Specialties
Strategy, Business Development, Mergers & Acquisitions, Joint Venture Management, Negotiation, Gas & LNG Marketing."

Target Market(s)

Oil and gas or energy companies of all sizes from large listed companies to start-ups - also service providers to the industry.

Industry/Entity Type

Oil And Gas

Contact Information for Business Card

KT Power Pty Ltd
Daniel Hobart
27C Lorne Avenue,
Kelmsdale,
WA 6093

Tel +61 455 823 617
email hobartdk@vellimo.net.au

```html
<!DOCTYPE html>
<html lang="en">
<head>
<meta charset="utf-8">
<title>KT Power Pty Ltd – Business Card</title>
<link rel="stylesheet" href="https://fonts.googleapis.com/css2?family=Source+Sans+3:wght@300;400;700&display=swap">
<style>
  :root {
    --backdrop: #c9c9c9;
    --card: #ffffff;
    --ink: #1d1d1d;
    --ink-soft: #2a2a2a;
    --growth-green: #6cbf46;
  }
  * { margin: 0; padding: 0; box-sizing: border-box; }
  html, body {
    width: 1200px;
    height: 897px;
    overflow: hidden;
    background: var(--backdrop);
    font-family: "Source Sans 3", "Myriad Pro", Arial, sans-serif;
  }
  .business-card {
    position: absolute;
    left: 235px;
    top: 238px;
    width: 730px;
    height: 420px;
    background: var(--card);
    overflow: hidden;
  }
  .growth-line {
    position: absolute;
    inset: 0;
    width: 730px;
    height: 420px;
  }
  .identity {
    position: absolute;
    left: 42px;
    top: 62px;
    color: var(--ink);
  }
  .company-name {
    font-weight: 700;
    font-size: 21px;
    line-height: 24px;
  }
  .person-name {
    font-weight: 700;
    font-size: 37px;
    line-height: 40px;
    margin-top: 2px;
    margin-left: 1px;
  }
  .contact {
    font-weight: 300;
    font-size: 21px;
    line-height: 29px;
    margin-top: 6px;
    color: var(--ink-soft);
  }
  .specialties {
    position: absolute;
    right: 27px;
    top: 162px;
    list-style: none;
    text-align: right;
    color: var(--ink);
    font-weight: 400;
    font-size: 22px;
    line-height: 40px;
    letter-spacing: 1.2px;
  }
</style>
</head>
<body>
  <section class="business-card" aria-label="KT Power Pty Ltd business card">
    <svg class="growth-line" viewBox="0 0 730 420" aria-hidden="true">
      <polyline points="250,432 355,385 416,249 509,228 564,159 650,141 736,-8"
                fill="none" stroke="var(--growth-green)" stroke-width="9"
                stroke-linejoin="miter"/>
    </svg>

    <div class="identity">
      <p class="company-name">KT Power Pty Ltd</p>
      <h1 class="person-name">Daniel Hobart</h1>
      <address class="contact" style="font-style:normal">
        27C Lorne Avenue, Kelmsdale, WA 6093<br>
        Tel +61 455 823 617<br>
        email hobartdk@vellimo.net.au
      </address>
    </div>

    <ul class="specialties">
      <li>Strategy</li>
      <li>Negotiation</li>
      <li>Gas &amp; LNG Marketing</li>
      <li>Business Development</li>
      <li>Mergers &amp; Acquisitions</li>
      <li>Joint Venture Management</li>
    </ul>
  </section>
</body>
</html>
```